GIDDY PANTRY needs a show poster

"Giddy Pantry" is a stand up comedy show. We need a fun, eye-catching poster. The taglines are "Loads of Laughter" and "Clean Comedy, Dirty Martinis." We are attaching our logo files and a vintage photo that we sometimes use, but they do not need to be a part of the poster. We like vintage* and retro* images but are open to the creativity of the designer.

* Added note: Vintage and Retro to us means 1950s-1970s design types, not distressed and worn looking. Color is good!

Target Market(s)

Women & Couples, Ages 30-70

Industry/Entity Type

Comedy

Requirements
Must have
• Title: Giddy Pantry
• Primary Tagline: Loads of Laughs
• Performers Names: Dana Whitlock & Lisa Ferrante
Nice to have
• Secondary Tagline: Clean Comedy, Dirty Martinis.
Should not have
• No cliche images of stand up comedy (spotlight, stage, microphone)

```html
<!DOCTYPE html>
<html lang="en">
<head>
<meta charset="utf-8">
<title>Giddy Pantry – Loads of Laughs</title>
<link rel="stylesheet" href="https://fonts.googleapis.com/css2?family=Montserrat:wght@600;800&family=Alfa+Slab+One&family=Leckerli+One&family=Bungee+Inline&display=swap">
<style>
  :root {
    --orange-deep: #de7328;
    --orange: #ea8f2e;
    --orange-light: #f2b24a;
    --cream: #f8f0b2;
    --cream-pale: #f9f1c6;
    --band: #f4bd35;
    --brown: #3b2520;
    --brown-panel: #4a2e27;
    --title-shadow: #e3741f;
  }
  * { margin: 0; padding: 0; box-sizing: border-box; }
  html, body { width: 856px; height: 1200px; overflow: hidden; background: var(--cream-pale); }
  .poster {
    position: relative;
    width: 856px;
    height: 1200px;
    overflow: hidden;
    font-family: "Montserrat", sans-serif;
  }
  .backdrop {
    position: absolute; inset: 0;
    background:
      radial-gradient(ellipse 420px 360px at 50% 62%, rgba(248,214,120,0.85), rgba(248,214,120,0) 70%),
      linear-gradient(180deg, var(--orange-deep) 0%, var(--orange) 40%, var(--orange-light) 62%, var(--cream) 78%, var(--cream-pale) 100%);
  }
  .brand {
    position: absolute; top: 150px; left: 0; width: 100%;
    text-align: center;
    font-weight: 800; font-size: 40px; line-height: 1;
    color: var(--brown); letter-spacing: 1px;
  }
  .secondary-tagline {
    position: absolute; top: 233px; left: 0; width: 100%; height: 68px;
    background: rgba(246, 196, 60, 0.85);
    display: flex; align-items: center; justify-content: center;
    font-weight: 800; font-size: 31px; letter-spacing: 1.5px;
    color: var(--brown);
  }
  .title-main {
    position: absolute; top: 330px; left: 0; width: 100%;
    text-align: center;
    font-family: "Alfa Slab One", serif;
    font-size: 178px; line-height: 1; letter-spacing: 4px;
    color: var(--cream);
    text-shadow: 5px 5px 0 var(--title-shadow), 9px 9px 0 rgba(210,100,30,0.6);
  }
  .title-script {
    position: absolute; top: 500px; left: 0; width: 100%;
    text-align: center;
    font-family: "Leckerli One", cursive;
    font-size: 120px; line-height: 1;
    color: var(--cream);
    -webkit-text-stroke: 3px var(--orange-deep);
    text-shadow: 6px 6px 0 var(--title-shadow);
  }
  .primary-tagline {
    position: absolute; top: 680px; left: 0; width: 100%;
    text-align: center;
    font-family: "Leckerli One", cursive;
    font-size: 72px; line-height: 0.95;
    color: var(--cream);
    -webkit-text-stroke: 2px var(--orange-deep);
    text-shadow: 4px 4px 0 var(--title-shadow);
  }
  .martini { position: absolute; top: 716px; width: 150px; height: 170px; }
  .martini--left { left: 60px; }
  .martini--right { left: 650px; }
  .performers-panel {
    position: absolute; top: 924px; left: 42px; width: 778px; height: 244px;
    background: var(--brown-panel);
  }
  .performers-label {
    position: absolute; top: 896px; left: 50%; transform: translateX(-50%);
    width: 270px; height: 52px;
  }
  .performers-label span {
    position: absolute; inset: 0;
    display: flex; align-items: center; justify-content: center;
    font-weight: 600; font-size: 20px; letter-spacing: 1.5px;
    color: var(--cream);
  }
  .performer-list {
    position: absolute; top: 968px; left: 42px; width: 778px;
    list-style: none; text-align: center;
    font-family: "Bungee Inline", sans-serif;
    font-size: 64px; line-height: 96px;
    color: var(--cream);
  }
</style>
</head>
<body>
<main class="poster">
  <div class="backdrop" role="img" aria-label="Retro orange sunburst background fading to cream"></div>

  <div class="brand">GIDDY PANTRY</div>

  <div class="secondary-tagline">CLEAN COMEDY, DIRTY MARTINIS</div>

  <h1 class="title-main">GIDDY</h1>
  <div class="title-script">Pantry</div>
  <p class="primary-tagline">Loads of<br>Laughs</p>

  <svg class="martini martini--left" viewBox="0 0 150 170" aria-hidden="true">
    <g fill="none" stroke="#fbeb9a" stroke-width="7" stroke-linejoin="round" stroke-linecap="round">
      <path d="M8 32 H122 L65 100 Z"/>
      <line x1="65" y1="100" x2="65" y2="158"/>
      <line x1="32" y1="160" x2="98" y2="160"/>
      <circle cx="122" cy="28" r="17"/>
    </g>
  </svg>
  <svg class="martini martini--right" viewBox="0 0 150 170" aria-hidden="true">
    <g fill="none" stroke="#fbeb9a" stroke-width="7" stroke-linejoin="round" stroke-linecap="round">
      <path d="M8 32 H122 L65 100 Z"/>
      <line x1="65" y1="100" x2="65" y2="158"/>
      <line x1="32" y1="160" x2="98" y2="160"/>
      <circle cx="122" cy="28" r="17"/>
    </g>
  </svg>

  <section class="performers-panel" aria-label="Performers"></section>
  <div class="performers-label">
    <svg viewBox="0 0 270 52" width="270" height="52" aria-hidden="true">
      <path d="M0 26 L22 6 H248 L270 26 L248 46 H22 Z" fill="var(--brown)" stroke="var(--cream)" stroke-width="2"/>
      <rect x="24" y="2" width="222" height="48" fill="var(--brown)" stroke="var(--cream)" stroke-width="2"/>
    </svg>
    <span>PERFORMERS</span>
  </div>
  <ul class="performer-list">
    <li>DANA WHITLOCK</li>
    <li>LISA FERRANTE</li>
  </ul>
</main>
</body>
</html>
```